LAMBERTINE KOVAX Vaporizer Company Thoughtful Kovax for a brighter daily path.

I need a logo design for a new Colorado based company. We wholesale exclusive vaporizer units. Smoke inhalation delivers damaging carcinogens and an onslaught of other damaging materials directly through the bronchial tree and into the lungs.What this means in more simple terms is that the vaporizer completely eliminates every last chemical that is directly associated with burning of the material.

It Company

```html
<!DOCTYPE html>
<html lang="en">
<head>
<meta charset="utf-8">
<title>Lambertine Kovax — Business Card</title>
<link href="https://fonts.googleapis.com/css2?family=Exo+2:wght@600&family=Open+Sans:wght@400&display=swap" rel="stylesheet">
<style>
  :root {
    --backdrop: #d2d2d2;
    --brand-green: #27ae5a;
    --brand-green-soft: #3cb76c;
    --paper: #f7f7f7;
  }
  html, body {
    margin: 0;
    padding: 0;
    width: 1200px;
    height: 1000px;
    overflow: hidden;
    background: var(--backdrop);
  }
  .card {
    position: absolute;
    left: 205px;
    top: 280px;
    width: 790px;
    height: 440px;
    background: var(--brand-green);
    overflow: hidden;
  }
  .card__accent {
    position: absolute;
    left: 95px;
    top: 40px;
    width: 420px;
    height: 420px;
    background: var(--brand-green-soft);
    opacity: 0.55;
  }
  .card__side-band {
    position: absolute;
    right: 95px;
    top: 0;
    width: 95px;
    height: 100%;
    background: var(--brand-green-soft);
    opacity: 0.8;
  }
  .brand {
    position: absolute;
    left: 165px;
    top: 262px;
    display: flex;
    align-items: center;
    gap: 14px;
  }
  .brand__mark {
    width: 40px;
    height: 40px;
    background: var(--paper);
  }
  .brand__name {
    font-family: "Exo 2", sans-serif;
    font-weight: 600;
    font-size: 40px;
    letter-spacing: 1px;
    color: var(--paper);
    line-height: 1;
  }
  .tagline-band {
    position: absolute;
    left: 160px;
    right: 0;
    top: 322px;
    height: 30px;
    background: var(--paper);
    display: flex;
    align-items: center;
    padding-left: 14px;
  }
  .tagline {
    font-family: "Open Sans", sans-serif;
    font-size: 19px;
    color: var(--brand-green);
  }
</style>
</head>
<body>
  <div class="card">
    <div class="card__accent" role="img" aria-label="Faint brand decoration"></div>
    <div class="card__side-band"></div>
    <div class="brand">
      <div class="brand__mark"></div>
      <div class="brand__name">LAMBERTINE KOVAX</div>
    </div>
    <div class="tagline-band">
      <span class="tagline">Thoughtful Kovax for a brighter daily path.</span>
    </div>
  </div>
</body>
</html>
```